Book cover design for 'Lantern Winter' novel

Title of book 'Lantern Winter'
Subtitle 'a Ness Orford novel'
Author 'T K Halvorsen'
Book genre 'novel - adventure'
Format ' eBook, paperback, audio, thumbnail'
Type 'Self-publishing through PVL'
Trim size 6 x 9
Back cover 'Seeking redemption on the Via de la Plata.
Ness Orford’s life changed forever in a moment of madness. Haunted by his crime, Ness feels a calling to seek redemption on the Camino de Santiago.
The daily toil of walking the Via de la Plata from Seville causes Ness to search his soul.
On The Way Ness encounters other pilgrims with their own personal reasons to answer the call of the camino.
Join Ness for the many highs and lows of camino life as he moves step by step closer to his goal.
Can the Camino give Ness peace of mind and stop his nightmares?'
Overall vision 'The front cover at the top should be the title:
Camino
Calling
This will fill about 20 per cent of the front cover. It must be centre justified. The title should use the same type face as the official Camino de Santiago road sign (see first download). The type should be in bright blue. The background should be in bright yellow.
Under the title should be an image of a path stretching to the horizon with the shadow of a pilgrim (see second download).
Superimposed on the image should be the words 'a Ness Orford novel' maybe using a type face similar to the street signage used in Spain (see third download).
At the bottom of the front cover should be the author's name 'Tom Halvorsen' in the same style as the blue and yellow title - BUT MUCH SMALLER.
On the SPINE of the book should be 'Lantern Winter' and 'Tom Halvorsen' in the blue text on yellow background.
On the back cover there should be a photograph (see fourth download) with the text UPDATE ON THE TEXT 'Seeking redemption on the Via de la Plata.
In a moment of madness Ness Orford’s life changed forever. Haunted by his atrocious act, he feels a calling to seek redemption on the Camino de Santiago.
The daily slog of walking the Via de la Plata from Seville causes Ness to search deep within his soul.
On The Way Ness encounters other pilgrims with their own personal reasons to answer the call of the Camino.
Can the Camino give Ness peace of mind and stop his nightmares?' with a three centimetre space at the bottom for bar code/ISBN and the author headshot photograph attached.

Target Market(s)

Readers who have walked the Camino de Santiago in Spain or who are interested

Requirements
Nice to have
• I would like my headshot (attached) included on the back cover

```html
<!DOCTYPE html>
<html lang="en">
<head>
<meta charset="utf-8">
<title>Lantern Winter – cover</title>
<link rel="stylesheet" href="https://fonts.googleapis.com/css2?family=Archivo+Black&family=Roboto:wght@400;700&family=Open+Sans:wght@300;400&display=swap">
<style>
  :root {
    --cream: #f8f6ea;
    --yellow: #f7b123;
    --blue: #0489d6;
    --ink: #1c1c1c;
    --rule: #a8a8a8;
    --white: #ffffff;
  }
  * { margin: 0; padding: 0; box-sizing: border-box; }
  html, body { width: 1200px; height: 880px; overflow: hidden; background: var(--cream); }
  .cover { position: relative; width: 1200px; height: 880px; }

  /* Back cover */
  .back { position: absolute; left: 0; top: 0; width: 547px; height: 880px; background: var(--cream); }
  .rule { position: absolute; left: 39px; width: 474px; height: 1px; background: var(--rule); }
  .rule--top { top: 100px; }
  .rule--bottom { top: 664px; }
  .back-heading {
    position: absolute; left: 59px; top: 134px;
    font-family: "Open Sans", sans-serif; font-weight: 300;
    font-size: 30px; line-height: 31px; color: var(--blue);
  }
  .blurb {
    position: absolute; left: 59px; top: 222px; width: 450px;
    font-family: "Open Sans", sans-serif; font-weight: 400;
    font-size: 17.6px; line-height: 38.6px; color: var(--ink);
  }
  .headshot {
    position: absolute; left: 51px; top: 684px; width: 122px; height: 122px;
    border-radius: 50%; border: 5px solid var(--blue);
    background: radial-gradient(circle at 50% 45%, #c9c3bd 0%, #8d8a88 60%, #4f5660 100%);
  }
  .author-caption {
    position: absolute; left: 61px; top: 812px;
    font-family: "Open Sans", sans-serif; font-size: 16px; color: var(--blue);
  }
  .isbn-box {
    position: absolute; left: 330px; top: 715px; width: 183px; height: 113px;
    background: var(--white);
    font-family: "Open Sans", sans-serif; font-size: 14.5px; line-height: 26px;
    color: var(--ink); text-align: center; padding-top: 5px;
  }

  /* Spine + front */
  .front { position: absolute; left: 547px; top: 0; width: 653px; height: 880px; background: var(--yellow); }
  .title {
    position: absolute; left: 150px; width: 490px; top: 30px; text-align: center;
    font-family: "Archivo Black", sans-serif; font-size: 86px; line-height: 92px;
    color: var(--blue); letter-spacing: -1px;
  }
  .series {
    position: absolute; left: 150px; width: 490px; top: 240px; text-align: center;
    font-family: "Roboto", sans-serif; font-weight: 700; font-size: 35px; color: var(--white);
  }
  .band { position: absolute; left: 0; width: 653px; height: 10px; background: var(--blue); }
  .band--top { top: 294px; }
  .band--bottom { top: 766px; }
  .scene {
    position: absolute; left: 0; top: 304px; width: 653px; height: 462px;
    background: linear-gradient(180deg, #9ea9b6 0%, #e9b896 18%, #f0c9a2 33%, #a8a78a 44%, #6f8f3c 52%, #5f8a2a 70%, #8b8a3e 100%);
  }
  .spine-title {
    position: absolute; left: 40px; top: 22px;
    writing-mode: vertical-rl;
    font-family: "Archivo Black", sans-serif; font-size: 31px; line-height: 1;
    color: var(--blue); letter-spacing: -0.5px;
  }
  .spine-author {
    position: absolute; left: 45px; top: 314px;
    writing-mode: vertical-rl;
    font-family: "Roboto", sans-serif; font-weight: 400; font-size: 24px; line-height: 1;
    color: var(--white);
  }
  .front-author {
    position: absolute; left: 150px; width: 490px; top: 790px; text-align: center;
    font-family: "Roboto", sans-serif; font-weight: 700; font-size: 42px; color: var(--blue);
  }
</style>
</head>
<body>
<div class="cover">
  <section class="back">
    <div class="rule rule--top"></div>
    <h2 class="back-heading">Seeking redemption on<br>the Via de la Plata.</h2>
    <p class="blurb">In a moment of madness Ness Orford’s life changed forever. Haunted by his atrocious act, he feels a calling to seek redemption on the Camino de Santiago. The daily slog of walking the Via de la Plata from Seville causes Ness to search deep within his soul. On The Way Ness encounters other pilgrims with their own personal reasons to answer the call of the Camino. Can the Camino give Ness peace of mind and stop his nightmares?</p>
    <div class="rule rule--bottom"></div>
    <div class="headshot" role="img" aria-label="Author headshot photograph"></div>
    <p class="author-caption">Tom Halvorsen</p>
    <div class="isbn-box">ISBN Number<br>&amp; barcode go here</div>
  </section>

  <section class="front">
    <div class="scene" role="img" aria-label="Photograph of a gravel path through green fields to the horizon at sunset, with a pilgrim's shadow on the path"></div>
    <div class="band band--top"></div>
    <div class="band band--bottom"></div>
    <div class="spine-title">Lantern Winter</div>
    <div class="spine-author">Tom Halvorsen</div>
    <h1 class="title">Lantern<br>Winter</h1>
    <p class="series">a Ness Orford novel</p>
    <p class="front-author">Tom Halvorsen</p>
  </section>
</div>
</body>
</html>
```